資格は全部で2種類あります。
各々コースが2つに分かれており、それぞれ初級・中級・上級があります。
コース・級ごとに色合いを変えていただければと思っております。
※デザイン2種:各6色(2つのコース×3つの級)の色合い変更

今回はコンペ形式にて1種類のデザインを募集させていただきます。
採用させていただいた方には、2種類ともデザインしていただければと思っております。

また、認定証のデザインをもとにした、認定カードのデザインもお願いいたします。
※認定証同様、デザイン2種各6色の色合い変更

採用報酬は、認定証・認定カードのすべてのデザインを含めた金額になります。
今回のコンペでは、下記2点の認定証のデザインを募集させていただきます。
①「創造育成指導員」という資格の「発達障がい支援コース」の「初級」
②「デジタル匠指導員」という資格の「IT実践コース」の「初級」

記載いただきたい項目は下記の通りになります。

・初級
・認定証
・発達障がい支援アドバイザー
・●●殿
・●●年●月●日
・あなたは当カリキュラムを修了されましたので、『初級・発達障がい支援アドバイザー』として認定いたします。
・NPO法人青葉学習推進会

・初級
・認定証
・IT実践アシスタント
・●●殿
・●●年●月●日
・あなたは当カリキュラムを修了されましたので、『初級・IT実践アシスタント』として認定いたします。
・NPO法人青葉学習推進会
認定証はカミノハコにて発注予定となっているため、イラストレーターのデータにて納品いただきますようお願いいたします。
テンプレートにつきましては、下記ギガファイル便のデータをご確認ください。
https://files.examplestore-transfer.jp/1008-a71c2e9b40f35d8862e1c7a04b5f2913e

また、ロゴや認定証のサンプルを添付させていただきます。
イラストレーターのデータにつきましては下記ギガファイル便をご確認ください。
https://files.examplestore-transfer.jp/1005-3b8e0f41c92d7a65e0b1f4d82c6a07e15

ゴールドを差し色とした素敵なデザインであったので選ばせていただきました。
ありがとうございました。

この度は弊社のコンペにご参加いただきありがとうございました。
また機会がございましたら、よろしくお願いいたします。

```html
<!DOCTYPE html>
<html lang="ja">
<head>
<meta charset="utf-8">
<title>認定証 初級 発達障がい支援アドバイザー</title>
<link rel="stylesheet" href="https://fonts.googleapis.com/css2?family=Shippori+Mincho+B1:wght@500;700;800&family=Cormorant+Garamond:wght@500&display=swap">
<style>
  :root {
    --paper: #fbf6ee;
    --paper-deep: #f4ead9;
    --gold: #c6a04c;
    --gold-light: #ecd694;
    --gold-soft: #f1e2b8;
    --gold-dark: #9c7426;
    --crimson: #9a1c22;
    --crimson-soft: #c98a7a;
    --ink: #2a2220;
  }
  * { margin: 0; padding: 0; box-sizing: border-box; }
  html, body { width: 851px; height: 1200px; overflow: hidden; background: var(--paper); }
  .certificate {
    position: relative;
    width: 851px;
    height: 1200px;
    background: radial-gradient(ellipse at 50% 45%, var(--paper) 55%, var(--paper-deep) 100%);
    font-family: "Shippori Mincho B1", serif;
    color: var(--ink);
    overflow: hidden;
  }
  .frame { position: absolute; inset: 0; }

  .emblem {
    position: absolute; left: 282px; top: 40px; width: 287px; height: 258px;
    border-radius: 40px;
    background: linear-gradient(180deg, var(--gold-light) 0%, var(--gold) 55%, var(--crimson-soft) 100%);
  }
  .grade {
    position: absolute; left: 0; width: 851px; top: 96px;
    text-align: center; font-size: 52px; font-weight: 800; line-height: 64px;
    color: var(--crimson); letter-spacing: 2px;
  }

  .laurel {
    position: absolute; top: 340px; width: 90px; height: 160px;
    border-radius: 45px;
    background: linear-gradient(180deg, var(--gold-soft), var(--gold-light));
  }
  .laurel--left { left: 236px; }
  .laurel--right { left: 525px; }

  .title {
    position: absolute; left: 0; width: 851px; top: 362px;
    text-align: center; font-size: 84px; font-weight: 800; line-height: 100px;
    color: var(--crimson); letter-spacing: 10px; text-indent: 10px;
  }
  .title-en {
    position: absolute; left: 0; width: 851px; top: 498px;
    text-align: center; font-family: "Cormorant Garamond", serif;
    font-size: 34px; font-weight: 500; line-height: 44px; color: var(--gold-dark); letter-spacing: 3px;
  }
  .qualification {
    position: absolute; left: 0; width: 851px; top: 540px;
    text-align: center; font-size: 34px; font-weight: 700; line-height: 46px;
    color: var(--crimson); letter-spacing: 3px;
  }
  .recipient {
    position: absolute; left: 185px; width: 482px; top: 686px; height: 48px;
    border-bottom: 1.5px solid var(--ink);
  }
  .recipient-honorific {
    position: absolute; right: 4px; bottom: 4px;
    font-size: 38px; font-weight: 700; line-height: 44px;
  }
  .issue-date {
    position: absolute; left: 0; width: 851px; top: 840px;
    text-align: center; font-size: 28px; font-weight: 700; line-height: 36px;
  }
  .issue-date span { display: inline-block; margin-left: 58px; }
  .issue-date span:first-child { margin-left: 0; }
  .statement {
    position: absolute; left: 0; width: 851px; top: 912px;
    text-align: center; font-size: 20px; font-weight: 500; line-height: 36px;
  }
  .issuer {
    position: absolute; left: 0; width: 851px; top: 1044px;
    display: flex; justify-content: center; align-items: center; gap: 14px;
  }
  .issuer-mark { width: 26px; height: 26px; border-radius: 50%; background: var(--crimson); }
  .issuer-name { font-size: 32px; font-weight: 800; line-height: 44px; color: var(--crimson); letter-spacing: 1px; }
</style>
</head>
<body>
<main class="certificate">
  <svg class="frame" width="851" height="1200" viewBox="0 0 851 1200" aria-hidden="true">
    <defs>
      <linearGradient id="goldLine" x1="0" y1="0" x2="1" y2="1">
        <stop offset="0" stop-color="#e4c77c"/>
        <stop offset="0.5" stop-color="#b8903c"/>
        <stop offset="1" stop-color="#e4c77c"/>
      </linearGradient>
    </defs>
    <rect x="18" y="18" width="815" height="1164" fill="none" stroke="url(#goldLine)" stroke-width="10"/>
    <rect x="36" y="36" width="779" height="1128" fill="none" stroke="#c6a04c" stroke-width="2.5"/>
    <rect x="44" y="44" width="763" height="1112" fill="none" stroke="#c6a04c" stroke-width="1"/>
  </svg>

  <div class="emblem" role="img" aria-label="金色のメダルと赤いリボン、三つの星の飾り"></div>
  <div class="grade">初級</div>

  <div class="laurel laurel--left" role="img" aria-label="金色の月桂樹の飾り"></div>
  <div class="laurel laurel--right" role="img" aria-label="金色の月桂樹の飾り"></div>

  <h1 class="title">認定証</h1>
  <p class="title-en">Advisor</p>
  <h2 class="qualification">発達障がい支援アドバイザー</h2>

  <div class="recipient"><span class="recipient-honorific">殿</span></div>

  <p class="issue-date"><span>令和</span><span>年</span><span>月</span><span>日</span></p>

  <p class="statement">
    あなたは当カリキュラムを修了されましたので、<br>
    『初級・発達障がい支援アドバイザー』として認定いたします。
  </p>

  <div class="issuer">
    <span class="issuer-mark"></span>
    <span class="issuer-name">NPO法人青葉学習推進会</span>
  </div>
</main>
</body>
</html>
```